Design a Trifold Brochure

Looking for design for a Trifold Brochure. Attached is our logo and a guide line to follow. The wording is to follow along with it and has not been corrected grammar wise. This will needed to be done. This all was done quickly so if you need to contact me rtk@brellowmail.com will let you email me.

Good Luck to the winner!

```html
<!DOCTYPE html>
<html lang="en">
<head>
<meta charset="utf-8">
<title>Sentinel Guard Systems – Trifold Brochure</title>
<link href="https://fonts.googleapis.com/css2?family=Roboto+Condensed:wght@300;400;700&family=Open+Sans:ital,wght@0,400;0,600;1,400&display=swap" rel="stylesheet">
<style>
  :root {
    --backdrop: #d6d6d6;
    --brand-blue: #2b2fb6;
    --brand-blue-deep: #1f2390;
    --brand-red: #8a1c22;
    --brand-red-deep: #6e1419;
    --paper: #ffffff;
    --paper-tint: #eceaea;
    --ink: #3a3a3a;
    --ink-soft: #f3dede;
  }
  * { box-sizing: border-box; margin: 0; padding: 0; }
  html, body { width: 901px; height: 1200px; overflow: hidden; }
  body {
    background: var(--backdrop);
    font-family: "Open Sans", Arial, sans-serif;
    position: relative;
  }
  .brochure {
    position: absolute;
    left: 30px; top: 275px;
    width: 840px; height: 650px;
    display: flex;
    box-shadow: 0 6px 24px rgba(0,0,0,.18);
  }
  .panel {
    position: relative;
    width: 280px; height: 650px;
    overflow: hidden;
    background: var(--paper);
  }
  .panel + .panel { border-left: 1px solid rgba(0,0,0,.06); }
  .band-svg { position: absolute; left: 0; width: 280px; display: block; }
  .photo { position: absolute; left: 0; width: 280px; }

  /* About panel */
  .about .photo {
    top: 0; height: 175px;
    background: radial-gradient(circle at 55% 55%, #3d6fa8 0%, #1d2a44 40%, #0e1320 100%);
  }
  .about-title {
    position: absolute; left: 30px; top: 210px;
    font-family: "Roboto Condensed", Arial, sans-serif;
    font-weight: 700; font-size: 17px; letter-spacing: .5px;
    color: var(--paper);
  }
  .about-copy {
    position: absolute; left: 30px; top: 245px; width: 222px;
    font-style: italic; font-size: 10.2px; line-height: 1.72;
    color: var(--ink-soft); text-align: justify;
  }
  .about-web {
    position: absolute; right: 22px; bottom: 22px;
    font-size: 9px; color: var(--ink-soft);
  }

  /* Services panel */
  .services-title {
    position: absolute; left: 0; top: 26px; width: 280px; text-align: center;
    font-family: "Roboto Condensed", Arial, sans-serif;
    font-weight: 700; font-size: 18px; color: var(--paper); letter-spacing: .5px;
  }
  .service-list {
    position: absolute; left: 34px; top: 90px; width: 230px;
    list-style: none;
    font-size: 10.5px; line-height: 1.55; color: var(--ink);
  }
  .service-list li { position: relative; padding-left: 14px; }
  .service-list li::before {
    content: ""; position: absolute; left: 0; top: 5px;
    width: 6px; height: 6px; border-radius: 50%; background: var(--brand-red);
  }
  .services .photo.monitoring {
    top: 205px; height: 160px;
    background: linear-gradient(180deg, #f4f4f4 0%, #c9cdd3 45%, #5b6068 70%, #e6e6e6 100%);
  }
  .slogan {
    position: absolute; left: 0; top: 368px; width: 280px; text-align: center;
    font-family: "Roboto Condensed", Arial, sans-serif;
    font-size: 12.5px; line-height: 1.25; color: var(--paper); letter-spacing: .4px;
  }
  .services .photo.service-map {
    top: 415px; height: 235px;
    background: linear-gradient(160deg, #e9e9e9 0%, #b8444a 35%, #8a1c22 65%, #efefef 100%);
  }

  /* Cover panel */
  .tagline {
    position: absolute; left: 0; top: 20px; width: 280px; text-align: center;
    font-family: "Roboto Condensed", Arial, sans-serif;
    font-size: 15px; color: var(--paper); letter-spacing: .4px;
  }
  .tagline strong { font-weight: 700; }
  .brand {
    position: absolute; left: 70px; top: 92px;
    display: flex; align-items: center; gap: 8px;
  }
  .brand-dot {
    width: 30px; height: 30px; border-radius: 50%;
    background: var(--brand-red); flex: none;
  }
  .brand-name {
    font-family: "Roboto Condensed", Arial, sans-serif;
    font-weight: 700; font-size: 15px; line-height: 1.05;
    color: var(--brand-red);
  }
  .cover .photo {
    top: 150px; height: 330px;
    background: radial-gradient(circle at 45% 45%, #e2c3a8 0%, #b88f78 30%, #6f6a72 70%, #3e3c46 100%);
  }
  .headline {
    position: absolute; left: 16px; top: 490px; width: 250px;
    font-family: "Roboto Condensed", Arial, sans-serif;
    font-size: 19px; line-height: 1.1; color: var(--paper);
    transform: rotate(-4deg); transform-origin: left top;
  }
  .headline strong { font-weight: 700; }
  .headline span { font-weight: 300; }
  .contact {
    position: absolute; left: 14px; top: 563px; width: 256px;
    display: flex; justify-content: space-between; align-items: center;
    font-size: 9px; color: var(--paper);
  }
  .contact-item { display: flex; align-items: center; gap: 5px; }
  .since {
    position: absolute; left: 0; bottom: 24px; width: 280px; text-align: center;
    font-family: "Roboto Condensed", Arial, sans-serif;
    font-weight: 700; font-size: 15px; color: var(--ink); letter-spacing: .5px;
  }
</style>
</head>
<body>
<main class="brochure">

  <!-- About panel -->
  <section class="panel about">
    <div class="photo" role="img" aria-label="Photo of hands around a glowing digital padlock"></div>
    <svg class="band-svg" style="top:140px" width="280" height="510" viewBox="0 0 280 510">
      <path d="M0 40 Q140 -10 280 40 L280 510 L0 510 Z" fill="var(--brand-red)"/>
    </svg>
    <h2 class="about-title">ABOUT US</h2>
    <p class="about-copy">Sentinel Guard Systems, Inc. was founded in 1982 in a small town. Our roots have grown deep since the first day of work. We have changed with the times and kept our values. All by ourselves, we built trust with every plant and home we serve. Today our systems protect more than a thousand sites across the region. Our team is dedicated to service, from the first call to the final install. We keep our word, we answer fast, and we stay with you. It is as simple as that.</p>
    <p class="about-web">www.sentinelguardsys.com</p>
  </section>

  <!-- Services panel -->
  <section class="panel services">
    <svg class="band-svg" style="top:0" width="280" height="80" viewBox="0 0 280 80">
      <path d="M0 0 H280 V58 L0 78 Z" fill="var(--brand-blue)"/>
    </svg>
    <h2 class="services-title">SERVICES</h2>
    <ul class="service-list">
      <li>Monitoring</li>
      <li>Service</li>
      <li>Inspections</li>
      <li>Security Evaluations</li>
      <li>Financing, Leasing and Service Contracts Available upon request</li>
    </ul>
    <div class="photo monitoring" role="img" aria-label="Photo of a security control room with a wall of camera monitors"></div>
    <svg class="band-svg" style="top:355px" width="280" height="65" viewBox="0 0 280 65">
      <path d="M0 8 L280 0 V52 L0 62 Z" fill="var(--brand-red)"/>
    </svg>
    <p class="slogan">SAVE MONEY, LIVE SAFER + SMILE<br>YOUR ON CAMERA</p>
    <div class="photo service-map" role="img" aria-label="Map of the service area across three southeastern states"></div>
  </section>

  <!-- Cover panel -->
  <section class="panel cover">
    <div class="photo" role="img" aria-label="Photo of a hand touching a glowing shield security icon"></div>
    <svg class="band-svg" style="top:0" width="280" height="160" viewBox="0 0 280 160">
      <path d="M0 0 H280 V52 L0 68 Z" fill="var(--brand-blue)"/>
      <path d="M0 68 L280 52 V150 L0 160 Z" fill="var(--paper-tint)"/>
    </svg>
    <p class="tagline">“ QUALITY THAT <strong>PROTECTS</strong> ”</p>
    <div class="brand">
      <span class="brand-dot"></span>
      <span class="brand-name">Sentinel Guard<br>Systems, Inc.</span>
    </div>
    <svg class="band-svg" style="top:470px" width="280" height="180" viewBox="0 0 280 180">
      <path d="M0 20 L280 0 V72 L0 90 Z" fill="var(--brand-red)"/>
      <path d="M0 90 L280 72 V104 L0 120 Z" fill="var(--brand-blue)"/>
      <path d="M0 120 L280 104 V180 H0 Z" fill="var(--paper)"/>
    </svg>
    <p class="headline"><strong>SOLUTION TO DRIVE YOUR</strong><br><strong>BUSINESS</strong> <span>THE NEXT LEVEL</span></p>
    <div class="contact">
      <span class="contact-item">
        <svg width="11" height="11" viewBox="0 0 12 12"><circle cx="6" cy="6" r="6" fill="#fff"/><path d="M4 3 L5.2 4.4 L4.6 5.2 Q5.4 6.8 6.8 7.4 L7.6 6.8 L9 8 L8.2 9 Q5 8.8 3 4 Z" fill="var(--brand-blue)"/></svg>
        555-013-4827
      </span>
      <span class="contact-item">
        <svg width="11" height="11" viewBox="0 0 12 12"><circle cx="6" cy="6" r="5.2" fill="none" stroke="#fff" stroke-width="1.2"/><path d="M1 6 H11 M6 1 Q3 6 6 11 M6 1 Q9 6 6 11" fill="none" stroke="#fff" stroke-width=".9"/></svg>
        www.sentinelguardsys.com
      </span>
    </div>
    <p class="since">SINCE 1982</p>
  </section>

</main>
</body>
</html>
```